Computer Training in the Education sector - Letterhead

We need a new letter head to be designed for the company. We provide computer training fro the Education Sector, both primary and private tertiary providers. The colours will need to tie in with the website www.crossingtheriver.co.nz.
The company name is Crossing the River with the tag line of Computer Training for Educators.
The footer will need to have the following detail...
0508 PCS TUTOR
021 847 193
www.crossingtheriver.co.nz / training@crossingtheriver.co.nz
Updates

Thanks for the designs so far.

Some have watermarks in the background. Please don't worry about using watermarks as I will not be using a watermark in in a final design.
Regards,
Warren

Thank you for all the designs and the effort. There was some great concepts that came through.

Cheers
Warren

Industry/Entity Type

Computer

```html
<!DOCTYPE html>
<html lang="en">
<head>
<meta charset="utf-8">
<title>Crossing the River – Letterhead</title>
<link rel="stylesheet" href="https://fonts.googleapis.com/css2?family=Arimo:wght@400&display=swap">
<style>
  :root {
    --backdrop: #e9e9e9;
    --paper: #ffffff;
    --brand-blue: #2e7fc3;
    --brand-orange: #f39a1e;
    --brand-green: #6cb33f;
    --grass-light: #8fd45a;
    --grass-mid: #4fae32;
    --grass-dark: #2f8a23;
  }
  html, body {
    margin: 0;
    padding: 0;
    width: 1200px;
    height: 795px;
    overflow: hidden;
    background: var(--backdrop);
    font-family: "Arimo", Arial, sans-serif;
  }
  .canvas {
    position: relative;
    width: 1200px;
    height: 795px;
  }
  .letterhead {
    position: absolute;
    left: 333px;
    top: 20px;
    width: 534px;
    height: 755px;
    background: var(--paper);
    box-shadow: 0 2px 10px rgba(0,0,0,0.12);
    overflow: hidden;
  }
  .brand {
    position: absolute;
    left: 48px;
    top: 44px;
  }
  .brand-name {
    display: flex;
    align-items: center;
    gap: 8px;
    font-size: 19px;
    font-weight: 400;
    color: var(--brand-blue);
    margin: 0;
  }
  .brand-dot {
    width: 14px;
    height: 14px;
    border-radius: 50%;
    background: var(--brand-orange);
  }
  .brand-tagline {
    margin: 8px 0 0 22px;
    font-size: 9.5px;
    color: var(--brand-blue);
  }
  .grass {
    position: absolute;
    left: 0;
    bottom: 0;
    width: 534px;
    height: 300px;
  }
  .contact {
    position: absolute;
    left: 48px;
    bottom: 80px;
    font-size: 10px;
    line-height: 1.35;
    white-space: nowrap;
  }
  .contact p { margin: 0; }
  .contact-phone { color: var(--brand-orange); }
  .contact-label { color: var(--brand-green); }
  .contact-value { color: var(--brand-blue); }
  .contact-gap { display: inline-block; width: 10px; }
</style>
</head>
<body>
<main class="canvas">
  <article class="letterhead">
    <header class="brand">
      <p class="brand-name"><span class="brand-dot"></span>Crossing the River</p>
      <p class="brand-tagline">Computer Training for Educators</p>
    </header>

    <svg class="grass" viewBox="0 0 534 300" preserveAspectRatio="none" role="img" aria-label="Illustration of green grass growing along the bottom edge, low at the left and tallest at the right">
      <defs>
        <linearGradient id="grass-fill" x1="0" y1="0" x2="0" y2="1">
          <stop offset="0" stop-color="var(--grass-light)"/>
          <stop offset="0.5" stop-color="var(--grass-mid)"/>
          <stop offset="1" stop-color="var(--grass-dark)"/>
        </linearGradient>
      </defs>
      <path d="M0 300 L0 270 C140 268 300 262 400 245 C460 232 505 180 534 110 L534 300 Z" fill="url(#grass-fill)"/>
    </svg>

    <footer class="contact">
      <p class="contact-phone">0508 PCS TUTOR</p>
      <p class="contact-phone">021 847 193</p>
      <p><span class="contact-label">web:</span> <span class="contact-value">www.crossingtheriver.co.nz</span><span class="contact-gap"></span><span class="contact-label">email:</span> <span class="contact-value">training@crossingtheriver.co.nz</span></p>
    </footer>
  </article>
</main>
</body>
</html>
```